Postcard Design

we are an environmentally safe cleaning company called Verdaplume Services, that specializes in post construction cleanup. for example, rehabbed houses and newly built commercial or residential space. we would like this mailer directed at the construction companies in order for them to call us before the property is ready to go to the buyer/client. we would like to see designs including a wood grain background and various earth toned colors (something very crisp, clean and not "flashy" marketing). It is important to convey we have flexibly with scheduling, competitive pricing, and that cleaning these properties not only enhances the contractors work but provides them with a happy customer. we are also on tobys board with a A rating and provide a 100% satisfaction guarentee

Industry/Entity Type

Construction

```html
<!DOCTYPE html>
<html lang="en">
<head>
<meta charset="utf-8">
<title>Verdaplume Services – Post Construction Cleanup Postcard</title>
<link href="https://fonts.googleapis.com/css2?family=Roboto+Condensed:ital,wght@0,400;0,700;1,700&family=Lilita+One&display=swap" rel="stylesheet">
<style>
  :root{
    --page:#f2f2f0;
    --card:#ffffff;
    --ink:#1b1b1b;
    --black:#161616;
    --orange:#f08a1c;
    --orange-deep:#c85a0c;
    --leaf:#7fb24a;
    --leaf-pale:#dcecc8;
    --leaf-badge:#6f9a3c;
    --lime-text:#a9d36a;
    --cream-text:#f4e9a0;
    --wood-light:#9a9690;
    --wood-dark:#5d5954;
    --sky:#e8ebee;
    --earth:#6e604d;
    --rule:#8a8a8a;
  }
  *{box-sizing:border-box;margin:0;padding:0}
  html,body{width:1200px;height:543px;overflow:hidden;background:var(--page)}
  body{font-family:"Roboto Condensed",Arial,sans-serif;color:var(--ink);position:relative}

  .postcard{position:absolute;top:72px;width:560px;height:400px;background:var(--card);
    box-shadow:0 3px 10px rgba(0,0,0,.18);overflow:hidden}
  .postcard--front{left:20px}
  .postcard--back{left:620px}

  /* front */
  .site-photo{position:absolute;left:0;top:120px;width:100%;height:280px;
    background:linear-gradient(180deg,var(--sky) 0%,#b9b6ae 35%,#8a7f70 65%,var(--earth) 100%)}
  .headline{position:absolute;left:26px;top:18px;transform:rotate(-4deg);transform-origin:left top}
  .headline__kicker{display:block;font-family:"Lilita One",sans-serif;font-size:30px;color:#fff8e0;
    -webkit-text-stroke:1.2px var(--black);letter-spacing:.5px;margin-left:38px;font-style:italic}
  .headline__main{display:block;font-family:"Lilita One",sans-serif;font-size:74px;line-height:.9;
    color:var(--orange);font-style:italic;-webkit-text-stroke:1.5px var(--orange-deep);
    text-shadow:3px 4px 0 var(--black)}
  .offer-disc{position:absolute;left:360px;top:22px;width:175px;height:175px;border-radius:50%;
    background:var(--black);color:#fff;text-align:center;display:flex;flex-direction:column;
    justify-content:center;line-height:1.2;font-size:13px}
  .offer-disc__call{font-weight:700;font-size:17px}
  .offer-disc__perk{font-weight:700;font-size:15px}
  .offer-disc__perk--green{color:var(--lime-text)}
  .offer-disc__perk--cream{color:var(--cream-text)}
  .offer-disc__green{color:var(--lime-text)}

  .brand-plate{position:absolute;width:215px;height:92px;background:var(--leaf-pale);
    border:2px solid #fff;display:flex;align-items:center;justify-content:center;gap:8px}
  .brand-plate__name{font-weight:700;font-size:36px;color:var(--ink);letter-spacing:-.5px}
  .brand-plate__dot{width:16px;height:16px;border-radius:50%;background:var(--leaf)}
  .postcard--front .brand-plate{left:16px;top:292px}

  /* back */
  .wood-panel{position:absolute;left:0;top:0;width:330px;height:100%;
    background:linear-gradient(90deg,var(--wood-light),var(--wood-dark) 45%,var(--wood-light) 75%,var(--wood-dark))}
  .postcard--back .brand-plate{left:30px;top:30px;width:270px;height:92px}
  .rating-line{position:absolute;left:0;width:330px;top:150px;text-align:center;color:#fff;
    font-weight:700;font-size:17px;text-shadow:1px 1px 2px #000}
  .guarantee-seal{position:absolute;left:90px;top:185px;width:150px;height:150px;border-radius:50%;
    background:radial-gradient(circle at 40% 35%,#8fbd55,var(--leaf-badge) 70%);border:3px solid #e9f2dc;
    color:#fff;text-align:center;display:flex;flex-direction:column;justify-content:center}
  .guarantee-seal__figure{font-weight:700;font-size:48px;line-height:1;text-shadow:1px 2px 2px rgba(0,0,0,.5)}
  .guarantee-seal__label{font-size:12px}
  .did-you-know{position:absolute;left:0;top:335px;width:315px;height:60px}
  .did-you-know svg{position:absolute;inset:0}
  .did-you-know__body{position:relative;padding:4px 0 0 10px;color:#fff;font-style:italic;font-weight:700;font-size:11.5px;line-height:1.25}
  .did-you-know__title{display:block;margin-bottom:2px}
  .did-you-know__text{display:block;padding-left:14px}

  .stamp-box{position:absolute;left:462px;top:30px;width:78px;height:88px;border:1px solid var(--ink)}
  .address-line{position:absolute;left:350px;width:192px;border-top:1px solid var(--rule)}
</style>
</head>
<body>

<section class="postcard postcard--front">
  <div class="site-photo" role="img" aria-label="Photograph of a construction site with scaffolding under a raised roadway and an orange crane"></div>
  <h1 class="headline">
    <span class="headline__kicker">Post Construction</span>
    <span class="headline__main">Cleanup</span>
  </h1>
  <div class="offer-disc">
    <span class="offer-disc__call">Call Us Today</span>
    <span>for</span>
    <span class="offer-disc__perk offer-disc__perk--green">Schedule Flexibility</span>
    <span class="offer-disc__perk offer-disc__perk--cream">Competitive pricing</span>
    <span>&amp; <span class="offer-disc__green">100%</span></span>
    <span class="offer-disc__green">Satisfaction Guarantee</span>
  </div>
  <div class="brand-plate"><span class="brand-plate__name">Verdaplume</span><span class="brand-plate__dot"></span></div>
</section>

<section class="postcard postcard--back">
  <div class="wood-panel" role="img" aria-label="Weathered grey wood plank texture"></div>
  <div class="brand-plate"><span class="brand-plate__name">Verdaplume</span><span class="brand-plate__dot"></span></div>
  <p class="rating-line">Check our A rating on tobys board</p>
  <div class="guarantee-seal">
    <span class="guarantee-seal__figure">100%</span>
    <span class="guarantee-seal__label">Satisfaction Guarantee</span>
  </div>
  <div class="did-you-know">
    <svg width="315" height="60" viewBox="0 0 315 60" aria-hidden="true">
      <polygon points="0,0 295,0 315,30 295,60 0,60" fill="rgba(235,235,235,.35)"/>
      <polygon points="0,0 95,0 103,10 95,18 0,18" fill="rgba(30,30,30,.75)"/>
    </svg>
    <p class="did-you-know__body">
      <span class="did-you-know__title">Did you know?</span>
      <span class="did-you-know__text">Cleaning these properties not only enhances the contractors work but provides them with a happy customer.</span>
    </p>
  </div>
  <div class="stamp-box"></div>
  <div class="address-line" style="top:150px"></div>
  <div class="address-line" style="top:205px"></div>
  <div class="address-line" style="top:260px"></div>
  <div class="address-line" style="top:315px"></div>
</section>

</body>
</html>
```